company, product, services, opportunity presentation

Pelminor is a Payment Services Processor with value added product and services. We are focusing on the Payment Industry, Retail Merchants and Financial institutions. We have built total solution on Nimbus cloud to provide API based payment solutions such as Issuing of cards, Acquiring of payment transactions, Fraud prevention, Ecommerce, with customer facing APPs to provide dynamic virtual payment , 2FA and Passwordless sign in. Our focus is B2B .
We are developing our sales/investor pitch deck with slides covering company information, Market challengers (problems) that we are solving , Opportunities in the regional markets as well as global addressable Market for Payment cards. Pelminor Product and services offerings to meet these challenges and opportunities.
Total Addressable Market statistics and data. Specific to virtual payment cards, Second factor authentication and digital ID (passwordless). Primarily data and justification for reducing Ecommerce card abandonment and increasing Authorization rates
Pelminor Team and advisors’ slide. Current pipeline and customers. Use cases or case studies. Highlighting competitive advantage and USP. target clients and current pipline. Financials and projected spend in the next 2 years including target amount to raise fund. Solution and services slides and timeine of activities /roadmap
We need a PPT design to project better look and feel, crisp and eye catching graphic and design of the slides. clearer representation of key or salient points in all slides and information.

Target Market(s)

Financial Institutions, Retail (Merchants), Fintechs, Transportation

Industry/Entity Type

Cards and Payments Industry . Fraud prevention . Digital ID

Font styles to use
Sans Serif

Colors
F0912C
F2A743
F7CA91
FBE8D2
FDF5EE
EE7325
F08F49
F5BC92
FAE3D3
FDF4ED
A7469A
B969AE
D3A5CF
EDDBEB
F8F0F9
6B429C
8869AF
B7A5CE
E3DAEB
F3F0F8

Requirements
Must have
• problem to be solved, market challenges, market opportunities, product features and functionality. Use cases, Financial spend and funding. Team members and advisors. Timeline of roadmap for 2 years. competitive advantage and USP. Benefits to each customer segments
Nice to have
• Provision for future development on product and services. potentially covering other target markets such as Airlines, Insurance

```html
<!DOCTYPE html>
<html lang="en">
<head>
<meta charset="utf-8">
<title>Pelminor – Credential Presentation</title>
<link href="https://fonts.googleapis.com/css2?family=Hind:wght@400;500;600;700&display=swap" rel="stylesheet">
<style>
:root{
  --purple:#7f2a7f;
  --purple-mid:#a7469a;
  --purple-soft:#edddeb;
  --purple-tint:#f8f0f9;
  --orange:#ee8a2a;
  --orange-deep:#ee7325;
  --orange-soft:#fbe8d2;
  --ink:#2b2230;
  --grey:#8a8a8a;
  --line:#c9c9c9;
  --stage:#ebebeb;
}
*{box-sizing:border-box;margin:0;padding:0}
html,body{width:1200px;height:800px;overflow:hidden}
body{background:var(--stage);font-family:"Hind",Arial,sans-serif;color:var(--ink);position:relative}
.slide{position:absolute;background:#fff;overflow:hidden}
.slide.large{width:554px;height:308px;top:29px}
.slide.small{width:366px;height:204px}
.abs{position:absolute}
.dash{position:absolute;height:2px;border-radius:2px}
.dash.p{background:var(--purple)} .dash.o{background:var(--orange)}
.slide-title{position:absolute;left:17px;top:18px;font-size:9.5px;font-weight:600;color:var(--purple);white-space:nowrap}
.slide-sub{position:absolute;left:17px;top:33px;font-size:6.5px;font-weight:600;color:var(--orange-deep)}
.brand{position:absolute;right:14px;top:10px;text-align:right;line-height:1}
.brand b{font-size:7.5px;font-weight:700;color:var(--purple)}
.brand span{display:block;font-size:4px;color:#c3c3c3;margin-top:2px}
.foot{position:absolute;left:17px;top:188px;font-size:5px;color:#555}
.page{position:absolute;right:17px;top:188px;font-size:5px;color:#ccc}
.page em{font-style:normal;color:var(--orange)}
svg.ic{position:absolute}
.cap{position:absolute;font-size:4px;font-weight:600;text-align:center;color:#222;white-space:nowrap}
/* cover */
.cover .logo{left:64px;top:100px;font-size:24px;font-weight:700;color:var(--purple)}
.cover .title{left:65px;top:156px;font-size:17px;font-weight:700;color:#222;letter-spacing:.2px}
.cover .lede{left:65px;top:183px;font-size:7px;color:#666}
.cover .date{left:65px;top:197px;font-size:7px;color:var(--orange)}
.cover .hero{left:277px;top:38px;width:222px;height:234px}
.cover .url{left:390px;top:144px;width:122px;height:20px;border-radius:10px;background:var(--orange);color:#fff;font-size:8px;display:flex;align-items:center;justify-content:center;box-shadow:0 3px 6px rgba(0,0,0,.15)}
.cover .copy,.verticals .copy{top:287px;font-size:8px;color:#333}
/* verticals */
.verticals .slide-title{left:25px;top:28px;font-size:15px}
.verticals .slide-sub{left:26px;top:51px;font-size:10px}
.verticals .brand{right:22px;top:17px}
.verticals .brand b{font-size:11px}.verticals .brand span{font-size:6.5px}
.vcard{position:absolute;width:110px;height:84px;background:#fff;border-radius:5px;box-shadow:2px 3px 6px rgba(0,0,0,.09);display:flex;flex-direction:column;align-items:center;justify-content:center;gap:8px;font-size:8.5px;font-weight:600;color:var(--orange-deep)}
.vcard.on{background:var(--purple);color:#fff;box-shadow:2px 3px 8px rgba(0,0,0,.2)}
.vcard svg{width:24px;height:24px}
/* services matrix */
.colhead{position:absolute;top:43px;height:14px;background:var(--orange);color:#fff;font-size:3.6px;font-weight:600;display:flex;align-items:center;justify-content:center;text-align:center;line-height:1.15;border-radius:1px}
.cell{position:absolute;height:15px;background:var(--purple-tint);border:.6px solid var(--purple-mid);color:var(--purple-mid);font-size:3.6px;display:flex;align-items:center;justify-content:center;text-align:center;line-height:1.1;border-radius:1px}
.band{position:absolute;left:14px;width:288px;height:11px;background:var(--purple);color:#fff;font-size:3.8px;display:flex;align-items:center;justify-content:center;border-radius:1px}
.pillar{position:absolute;top:43px;width:13px;height:132px;background:var(--purple);color:#fff;font-size:3.6px;writing-mode:vertical-rl;display:flex;align-items:center;justify-content:center;border-radius:1px}
.net{position:absolute;left:265px;font-size:5.5px;font-weight:700;color:var(--purple)}
/* pills */
.pill-rows{position:absolute;left:0;right:0;top:64px;display:flex;flex-direction:column;align-items:center;gap:7px}
.pill-row{display:flex;gap:5px}
.pill{height:20px;padding:0 11px;display:flex;align-items:center;font-size:5px;font-weight:600;color:#fff;border-radius:1px}
.pill.o{background:var(--orange)}.pill.p{background:var(--purple)}
/* ecosystem */
.frame-o{position:absolute;border:1.6px solid var(--orange);border-radius:2px}
.frame-p{position:absolute;border:1.6px solid var(--purple);border-radius:3px}
.frame-b{position:absolute;border:1px solid #6ec1e4;border-radius:2px}
.tile{position:absolute;background:var(--purple);color:#fff;font-weight:600;display:flex;align-items:center;justify-content:center;text-align:center;line-height:1.15;border-radius:1px}
.tile.mini{font-size:3.2px;font-weight:500;line-height:1.1;padding:0 1px}
.legend{position:absolute;border:1px solid var(--orange-soft);background:#fff;font-size:4.5px;color:#222}
.legend .h{position:absolute;left:0;right:0;top:8px;text-align:center;font-weight:600}
.hline{position:absolute;height:0;border-top:1px solid #bdbdbd}
.hline.dash{border-top:1px dashed #bdbdbd}
.vline{position:absolute;width:0;border-left:1px solid #bdbdbd}
.netname{font-weight:700;color:var(--purple);position:absolute;white-space:nowrap}
.badge{position:absolute;background:var(--orange);border-radius:50%;border:1.5px solid #fff}
</style>
</head>
<body>
<svg width="0" height="0" style="position:absolute">
  <defs>
    <symbol id="i-shop" viewBox="0 0 24 24"><rect x="3" y="9" width="18" height="13" fill="#3aa3c9"/><path d="M2 4h20v5H2z" fill="#f0912c"/><path d="M2 4h4v5H2zM10 4h4v5h-4zM18 4h4v5h-4z" fill="#4caf50"/><rect x="6" y="13" width="5" height="9" fill="#2d3e50"/><rect x="13" y="13" width="6" height="5" fill="#cfe9f5"/></symbol>
    <symbol id="i-pos" viewBox="0 0 24 24"><rect x="6" y="2" width="12" height="20" rx="2" fill="#2d3e50"/><rect x="8" y="4" width="8" height="5" fill="#9ad3ea"/><g fill="#e0e0e0"><rect x="8" y="11" width="2" height="2"/><rect x="11" y="11" width="2" height="2"/><rect x="14" y="11" width="2" height="2"/><rect x="8" y="14" width="2" height="2"/><rect x="11" y="14" width="2" height="2"/><rect x="14" y="14" width="2" height="2"/></g></symbol>
    <symbol id="i-atm" viewBox="0 0 24 24"><path d="M6 2h12v20H6z" fill="#b7c4cc"/><rect x="8" y="4" width="8" height="6" fill="#3aa3c9"/><rect x="8" y="12" width="8" height="2" fill="#2d3e50"/><rect x="8" y="16" width="8" height="4" fill="#8a99a3"/></symbol>
    <symbol id="i-bank" viewBox="0 0 24 24"><circle cx="12" cy="12" r="10" fill="#e6f3f9" stroke="#3aa3c9" stroke-width="1.5"/><path d="M6 10l6-4 6 4zM7 11h2v6H7zM11 11h2v6h-2zM15 11h2v6h-2zM6 17h12v1.5H6z" fill="#3aa3c9"/></symbol>
    <symbol id="i-server" viewBox="0 0 24 24"><g fill="none" stroke="#2d3e50" stroke-width="1.6"><rect x="4" y="3" width="16" height="5" rx="1"/><rect x="4" y="10" width="16" height="5" rx="1"/><rect x="4" y="17" width="16" height="5" rx="1"/></g></symbol>
    <symbol id="i-lock" viewBox="0 0 24 24"><path d="M8 10V7a4 4 0 018 0v3" fill="none" stroke="#ee7325" stroke-width="2"/><rect x="5" y="10" width="14" height="11" rx="1.5" fill="#f0912c"/><path d="M0 15h5M19 15h5" stroke="#555" stroke-width="1"/></symbol>
    <symbol id="i-laptop" viewBox="0 0 24 24"><rect x="5" y="5" width="14" height="10" fill="none" stroke="#2d3e50" stroke-width="1.6"/><path d="M2 18h20" stroke="#2d3e50" stroke-width="2"/></symbol>
    <symbol id="i-cloud" viewBox="0 0 24 16"><path d="M6 15a5 5 0 01-.5-10A6 6 0 0117 4a4.5 4.5 0 011 11z" fill="#9ad3ea" stroke="#3aa3c9"/></symbol>
    <symbol id="i-cards" viewBox="0 0 40 14"><rect x="1" y="2" width="15" height="10" rx="1.5" fill="none" stroke="#4caf50" stroke-width="1.3"/><path d="M1 5h15" stroke="#4caf50" stroke-width="1.3"/><rect x="22" y="2" width="15" height="10" rx="1.5" fill="none" stroke="#e53935" stroke-width="1.3"/><path d="M22 5h15" stroke="#e53935" stroke-width="1.3"/></symbol>
  </defs>
</svg>

<!-- Cover -->
<section class="slide large cover" style="left:36px">
  <div class="abs logo">Pelminor</div>
  <div class="dash p" style="left:65px;top:148px;width:22px;height:3px"></div>
  <div class="dash o" style="left:91px;top:148px;width:8px;height:3px"></div>
  <div class="abs title">PRESENTATION TITTLE</div>
  <div class="abs lede">Here a Place for Credintial Presentation</div>
  <div class="abs date">July 2022</div>
  <svg class="abs hero" viewBox="0 0 222 234" role="img" aria-label="Photo of blue glowing fibre optic strands on a dark background">
    <defs><radialGradient id="fibre" cx="35%" cy="45%" r="70%"><stop offset="0" stop-color="#3a3fb0"/><stop offset=".45" stop-color="#171842"/><stop offset="1" stop-color="#0d0d1c"/></radialGradient></defs>
    <path d="M90 6Q111-6 132 6L200 46Q222 58 222 84V150Q222 176 200 188L132 228Q111 240 90 228L22 188Q0 176 0 150V84Q0 58 22 46Z" fill="url(#fibre)"/>
  </svg>
  <div class="abs url">www.pelminor.example</div>
  <div class="abs copy" style="left:27px">© Pelminor Pte. Ltd.</div>
</section>

<!-- Target verticals -->
<section class="slide large verticals" style="left:610px">
  <div class="dash p" style="left:26px;top:20px;width:22px;height:3px"></div>
  <div class="dash o" style="left:53px;top:20px;width:8px;height:3px"></div>
  <div class="slide-title">Business Solutions &amp; Client Verticals</div>
  <div class="slide-sub">Target Client Verticals</div>
  <div class="brand"><b>Pelminor</b><span>Online Payment Security</span></div>
  <div class="vcard" style="left:81px;top:83px"><svg viewBox="0 0 24 24"><circle cx="11" cy="11" r="8" fill="none" stroke="#ee7325" stroke-width="2.4"/><text x="11" y="15" font-size="10" text-anchor="middle" fill="#ee7325" font-weight="700">$</text><path d="M14 14l7 7" stroke="#ee7325" stroke-width="2.4"/></svg>Finance Instituions</div>
  <div class="vcard on" style="left:231px;top:83px"><svg viewBox="0 0 24 24"><path d="M2 12h20M12 12l-5-8h3l6 8-6 8H7zM4 12l-2-4M4 12l-2 4" stroke="#f0912c" stroke-width="2.2" fill="#f0912c" stroke-linejoin="round"/></svg>Airlanes</div>
  <div class="vcard" style="left:367px;top:83px"><svg viewBox="0 0 24 24"><path d="M3 10l9-7 9 7v11H3z" fill="#ee7325"/><g fill="#fff"><rect x="7" y="11" width="3" height="3"/><rect x="14" y="11" width="3" height="3"/><rect x="10" y="16" width="4" height="5"/></g></svg>Hotels</div>
  <div class="vcard" style="left:81px;top:180px"><svg viewBox="0 0 24 24"><rect x="3" y="4" width="18" height="5" fill="#ee7325"/><rect x="4" y="10" width="16" height="11" fill="none" stroke="#ee7325" stroke-width="2"/><rect x="7" y="13" width="4" height="8" fill="#ee7325"/><rect x="13" y="13" width="5" height="4" fill="#ee7325"/></svg>Merchant Aggregators</div>
  <div class="vcard" style="left:231px;top:180px"><svg viewBox="0 0 24 24"><path d="M2 4h3l3 11h11l2-8H7" fill="none" stroke="#ee7325" stroke-width="2"/><circle cx="9" cy="19" r="1.8" fill="#ee7325"/><circle cx="17" cy="19" r="1.8" fill="#ee7325"/></svg>Large Retailers</div>
  <div class="vcard" style="left:367px;top:180px"><svg viewBox="0 0 24 24"><circle cx="12" cy="12" r="7" fill="none" stroke="#ee7325" stroke-width="2"/><path d="M12 1v5M12 18v5M1 12h5M18 12h5" stroke="#ee7325" stroke-width="2"/><text x="12" y="15.5" font-size="9" text-anchor="middle" fill="#ee7325" font-weight="700">$</text></svg>SME’s</div>
  <div class="abs copy" style="left:26px">© Pelminor Pte. Ltd.</div>
  <div class="abs" style="right:25px;top:287px;font-size:9px;color:#ccc">page <span style="color:var(--orange)">2</span></div>
</section>

<!-- Services matrix -->
<section class="slide small" style="left:37px;top:350px">
  <div class="dash p" style="left:17px;top:13px;width:14px"></div><div class="dash o" style="left:35px;top:13px;width:6px"></div>
  <div class="slide-title">Business Solutions &amp; Client Verticals</div>
  <div class="brand"><b>Pelminor</b><span>Online Payment Security</span></div>
  <div class="colhead" style="left:14px;width:59px">ISSUER SERVICES</div>
  <div class="colhead" style="left:76px;width:42px">CONTACTLESS<br>PAYMENTS</div>
  <div class="colhead" style="left:122px;width:87px">ACQUIRER<br>SERVICES</div>
  <div class="colhead" style="left:212px;width:44px">E-COMMERCE<br>SERVICES</div>
  <div class="colhead" style="left:259px;width:43px">PAYMENT<br>NETWORKS</div>
  <div class="cell" style="left:14px;top:60px;width:11px;height:69px;writing-mode:vertical-rl;transform:rotate(180deg);font-size:3.2px">Dynamic Virtual Card/Token Vexpay ©</div>
  <div class="cell" style="left:28px;top:60px;width:45px">Debit Cards</div>
  <div class="cell" style="left:28px;top:78px;width:45px">Virtual &amp; Prepaid<br>Cards</div>
  <div class="cell" style="left:28px;top:96px;width:45px">Credit Cards</div>
  <div class="cell" style="left:28px;top:114px;width:45px">Corporate Cards</div>
  <div class="cell" style="left:76px;top:60px;width:42px">NFC</div>
  <div class="cell" style="left:76px;top:78px;width:42px">E-Wallets</div>
  <div class="cell" style="left:76px;top:96px;width:42px">QR Code</div>
  <div class="cell" style="left:76px;top:114px;width:42px">Tap to Phone</div>
  <div class="cell" style="left:122px;top:60px;width:42px">Merchant<br>Management</div>
  <div class="cell" style="left:122px;top:78px;width:42px">POS/mPOS<br>Acquiring</div>
  <div class="cell" style="left:122px;top:96px;width:42px">Merchant Loyalty</div>
  <div class="cell" style="left:122px;top:114px;width:42px">Merchant Portal</div>
  <div class="cell" style="left:167px;top:60px;width:42px">ATM/Kiosk<br>Acquiring</div>
  <div class="cell" style="left:167px;top:78px;width:42px">ATM Scenario<br>Builder</div>
  <div class="cell" style="left:167px;top:96px;width:42px">ATM/Kiosk<br>Monitoring</div>
  <div class="cell" style="left:167px;top:114px;width:42px">ATM/Kiosk<br>Management</div>
  <div class="cell" style="left:212px;top:60px;width:44px">E-Commerce<br>Acquiring</div>
  <div class="cell" style="left:212px;top:78px;width:44px">3D Secure</div>
  <div class="cell" style="left:212px;top:96px;width:44px">BNPL</div>
  <div class="cell" style="left:212px;top:114px;width:44px">Loyalty</div>
  <div class="net" style="top:62px">Veltra</div>
  <div class="net" style="top:80px">Marlo</div>
  <div class="net" style="top:98px">Unipax</div>
  <div class="net" style="top:116px">Dinora</div>
  <div class="band" style="top:133px">Deep Analytical Services</div>
  <div class="band" style="top:148px">Real-time Fraud Prevention</div>
  <div class="band" style="top:163px">API Stack</div>
  <div class="pillar" style="left:305px">Project &amp; Program Management</div>
  <div class="pillar" style="left:321px">Solution Consulting</div>
  <div class="pillar" style="left:337px">Discovery Workshops</div>
  <div class="foot">© Pelminor Pte. Ltd.</div><div class="page">page <em>3</em></div>
</section>

<!-- Solutions pills -->
<section class="slide small" style="left:417px;top:350px">
  <div class="dash p" style="left:17px;top:13px;width:14px"></div><div class="dash o" style="left:35px;top:13px;width:6px"></div>
  <div class="slide-title">Business Solutions &amp; Client Verticals</div>
  <div class="brand"><b>Pelminor</b><span>Online Payment Security</span></div>
  <div class="pill-rows">
    <div class="pill-row"><div class="pill o" style="padding:0 13px">Digital Payment Processing</div><div class="pill p">Fraud Prevention / Detection</div><div class="pill o" style="padding:0 14px">Corporate Cards</div></div>
    <div class="pill-row"><div class="pill p" style="padding:0 14px">Keyless Entry</div><div class="pill o">Loyalty Monetization</div><div class="pill p">Single ID Management</div><div class="pill p" style="padding:0 14px">Travel Cards</div></div>
    <div class="pill-row"><div class="pill o">Fleet &amp; Fuel Cards</div><div class="pill p">OTP/2FA Passwordless Login</div><div class="pill o">Enhanced Identity Verification</div></div>
  </div>
  <div class="foot">© Pelminor Pte. Ltd.</div><div class="page">page <em>4</em></div>
</section>

<!-- Ecosystem overview -->
<section class="slide small" style="left:796px;top:350px">
  <div class="dash p" style="left:17px;top:13px;width:14px"></div><div class="dash o" style="left:35px;top:13px;width:6px"></div>
  <div class="slide-title">Pelminor Payment Ecosystem</div>
  <div class="brand"><b>Pelminor</b><span>Online Payment Security</span></div>
  <div class="abs" style="left:32px;top:45px;font-size:4.5px;font-weight:600">Acquirers</div>
  <div class="frame-b" style="left:12px;top:55px;width:64px;height:24px"></div>
  <svg class="ic" style="left:21px;top:58px" width="8" height="8"><use href="#i-shop"/></svg>
  <svg class="ic" style="left:43px;top:58px" width="8" height="8"><use href="#i-pos"/></svg>
  <svg class="ic" style="left:60px;top:58px" width="8" height="8"><use href="#i-atm"/></svg>
  <div class="cap" style="left:14px;top:70px;width:24px;font-size:3.4px">Merchant</div>
  <div class="cap" style="left:38px;top:70px;width:16px;font-size:3.4px">POS</div>
  <div class="cap" style="left:56px;top:70px;width:16px;font-size:3.4px">ATM</div>
  <div class="vline" style="left:44px;top:79px;height:12px"></div>
  <svg class="ic" style="left:15px;top:90px" width="58" height="38" viewBox="0 0 24 16"><path d="M6 15a5 5 0 01-.5-10A6 6 0 0117 4a4.5 4.5 0 011 11z" fill="#fff" stroke="#2b2230" stroke-width=".8"/></svg>
  <div class="netname" style="left:29px;top:104px;font-size:4px">Veltra</div><div class="netname" style="left:47px;top:104px;font-size:4px">Unipax</div>
  <div class="netname" style="left:26px;top:113px;font-size:3.6px">Marlo · Jexa · Dinora</div>
  <svg class="ic" style="left:31px;top:130px" width="22" height="8"><use href="#i-cards"/></svg>
  <div class="cap" style="left:22px;top:139px;width:40px;font-size:3.3px;font-weight:400;line-height:1.3">Card present<br>&amp;<br>Card not present</div>
  <div class="hline dash" style="left:75px;top:105px;width:15px"></div>
  <div class="frame-o" style="left:90px;top:67px;width:131px;height:64px"></div>
  <div class="abs" style="left:105px;top:74px;font-size:5.5px;font-weight:700;color:var(--purple)">Pelminor</div>
  <div class="abs" style="left:153px;top:71px;width:10px;height:10px;border-radius:50%;background:#3d9b4f"></div>
  <div class="abs" style="left:185px;top:72px;width:12px;height:8px;border-radius:4px;background:var(--orange)"></div>
  <div class="abs" style="left:95px;top:86px;width:122px;height:38px;background:var(--orange-soft)"></div>
  <div class="tile mini" style="left:97px;top:88px;width:18px;height:16px">Switch<br>&amp; CMS</div>
  <div class="tile mini" style="left:118px;top:88px;width:18px;height:16px">POS<br>Pre-host</div>
  <div class="tile mini" style="left:139px;top:88px;width:20px;height:16px">Pelminor<br>APIs</div>
  <div class="tile mini" style="left:162px;top:88px;width:18px;height:16px">API stack<br>&amp; Portal</div>
  <div class="tile mini" style="left:183px;top:88px;width:31px;height:16px">Merchant<br>Portal Server</div>
  <div class="tile mini" style="left:97px;top:107px;width:18px;height:16px">E-KYC<br>Host</div>
  <div class="tile mini" style="left:118px;top:107px;width:18px;height:16px">Vexpay<br>Appliance</div>
  <div class="tile mini" style="left:139px;top:107px;width:20px;height:16px">HSM</div>
  <div class="tile mini" style="left:162px;top:107px;width:18px;height:16px">POS<br>Simulator</div>
  <div class="tile mini" style="left:183px;top:107px;width:31px;height:16px">ATM Sim &amp;<br>Scenario Builder</div>
  <div class="hline" style="left:221px;top:99px;width:21px"></div>
  <svg class="ic" style="left:226px;top:94px" width="10" height="10"><use href="#i-lock"/></svg>
  <div class="abs" style="left:240px;top:96px;font-size:3.6px;font-weight:600">VPN</div>
  <div class="vline" style="left:236px;top:69px;height:63px"></div>
  <div class="hline" style="left:236px;top:69px;width:10px"></div><div class="hline" style="left:236px;top:132px;width:10px"></div>
  <div class="abs" style="left:270px;top:93px;width:58px;height:17px;background:var(--orange);color:var(--purple);font-size:3.8px;font-weight:600;display:flex;align-items:center;justify-content:center;text-align:center;line-height:1.15">Pelminor Client<br>Institutions</div>
  <div class="frame-o" style="left:246px;top:56px;width:106px;height:26px"></div>
  <div class="badge" style="left:241px;top:50px;width:12px;height:12px"></div>
  <div class="abs" style="left:257px;top:48px;font-size:4px;font-weight:600">Institution 1</div>
  <div class="frame-o" style="left:246px;top:127px;width:106px;height:26px"></div>
  <div class="badge" style="left:241px;top:147px;width:12px;height:12px"></div>
  <div class="abs" style="left:261px;top:155px;font-size:4px;color:var(--orange)">Institution 2</div>
  <svg class="ic" style="left:256px;top:62px" width="90" height="9"><use href="#i-pos" x="0" width="9"/><use href="#i-atm" x="20" width="9"/><use href="#i-bank" x="40" width="9"/><use href="#i-shop" x="60" width="9"/><use href="#i-server" x="80" width="9"/></svg>
  <div class="cap" style="left:251px;top:74px;width:19px;font-size:3px">POS</div><div class="cap" style="left:271px;top:74px;width:19px;font-size:3px">ATM</div><div class="cap" style="left:291px;top:74px;width:19px;font-size:3px">CBS</div><div class="cap" style="left:311px;top:74px;width:19px;font-size:3px">Merchant</div><div class="cap" style="left:331px;top:74px;width:19px;font-size:3px">Other host</div>
  <svg class="ic" style="left:256px;top:133px" width="90" height="9"><use href="#i-pos" x="0" width="9"/><use href="#i-atm" x="20" width="9"/><use href="#i-bank" x="40" width="9"/><use href="#i-shop" x="60" width="9"/><use href="#i-server" x="80" width="9"/></svg>
  <div class="cap" style="left:251px;top:145px;width:19px;font-size:3px">POS</div><div class="cap" style="left:271px;top:145px;width:19px;font-size:3px">ATM</div><div class="cap" style="left:291px;top:145px;width:19px;font-size:3px">CBS</div><div class="cap" style="left:311px;top:145px;width:19px;font-size:3px">Merchant</div><div class="cap" style="left:331px;top:145px;width:19px;font-size:3px">Other host</div>
  <div class="legend" style="left:90px;top:145px;width:33px;height:31px;font-size:3px"><div class="h" style="top:5px">Payment network</div><div class="hline" style="left:5px;top:15px;width:12px;border-color:#333"></div><div class="abs" style="left:19px;top:13px">Online</div><div class="hline dash" style="left:5px;top:23px;width:12px;border-color:#333"></div><div class="abs" style="left:19px;top:21px">Offline</div></div>
  <svg class="ic" style="left:147px;top:139px" width="10" height="7"><use href="#i-cloud"/></svg>
  <div class="abs" style="left:141px;top:148px;font-size:3.4px;color:#555">Internet</div>
  <div class="frame-b" style="left:173px;top:145px;width:49px;height:31px"></div>
  <svg class="ic" style="left:180px;top:150px" width="13" height="13"><use href="#i-laptop"/></svg>
  <div class="abs" style="left:197px;top:149px;width:14px;height:14px;border-radius:50%;background:#8bc34a" role="img" aria-label="Illustrated customer avatar"></div>
  <div class="cap" style="left:173px;top:166px;width:49px;font-size:3.4px">Institution Merchant</div>
  <div class="foot">© Pelminor Pte. Ltd.</div><div class="page">page <em>5</em></div>
</section>

<!-- Acquirers -->
<section class="slide small" style="left:37px;top:567px">
  <div class="dash p" style="left:17px;top:13px;width:14px"></div><div class="dash o" style="left:35px;top:13px;width:6px"></div>
  <div class="slide-title">Pelminor Payment Ecosystem</div>
  <div class="slide-sub"># 1. Acquirers</div>
  <div class="brand"><b>Pelminor</b><span>Online Payment Security</span></div>
  <div class="frame-p" style="left:31px;top:72px;width:120px;height:51px"></div>
  <svg class="ic" style="left:44px;top:82px" width="20" height="20"><use href="#i-shop"/></svg>
  <svg class="ic" style="left:84px;top:82px" width="20" height="20"><use href="#i-pos"/></svg>
  <svg class="ic" style="left:120px;top:82px" width="20" height="20"><use href="#i-atm"/></svg>
  <div class="cap" style="left:34px;top:108px;width:40px;font-size:4.6px">Merchant</div>
  <div class="cap" style="left:78px;top:109px;width:30px;font-size:4.6px">POS</div>
  <div class="cap" style="left:115px;top:109px;width:30px;font-size:4.6px">ATM</div>
  <div class="hline dash" style="left:151px;top:99px;width:215px"></div>
  <svg class="ic" style="left:213px;top:68px" width="76" height="50" viewBox="0 0 24 16"><path d="M6 15a5 5 0 01-.5-10A6 6 0 0117 4a4.5 4.5 0 011 11z" fill="#fff" stroke="#2b2230" stroke-width=".7"/></svg>
  <div class="netname" style="left:232px;top:88px;font-size:6px">Veltra</div><div class="netname" style="left:256px;top:88px;font-size:6px">Unipax</div>
  <div class="netname" style="left:228px;top:99px;font-size:5.5px">Marlo · Jexa · Dinora</div>
  <div class="legend" style="left:95px;top:140px;width:56px;height:37px"><div class="h">Payment network</div><div class="hline" style="left:7px;top:21px;width:22px;border-color:#333"></div><div class="abs" style="left:33px;top:18px">Online</div><div class="hline dash" style="left:7px;top:29px;width:22px;border-color:#333"></div><div class="abs" style="left:33px;top:26px">Offline</div></div>
  <div class="legend" style="left:223px;top:140px;width:56px;height:37px;border-color:#ccc"><svg class="ic" style="left:12px;top:4px" width="32" height="11"><use href="#i-cards"/></svg><div class="cap" style="left:0;top:16px;width:56px;font-size:4.4px;font-weight:400;line-height:1.3">Card present<br>&amp;<br>Card not present</div></div>
  <div class="foot">© Pelminor Pte. Ltd.</div><div class="page">page <em>6</em></div>
</section>

<!-- Process -->
<section class="slide small" style="left:417px;top:567px">
  <div class="dash p" style="left:17px;top:13px;width:14px"></div><div class="dash o" style="left:35px;top:13px;width:6px"></div>
  <div class="slide-title">Pelminor Payment Ecosystem</div>
  <div class="slide-sub"># 2. Process</div>
  <div class="brand"><b>Pelminor</b><span>Online Payment Security</span></div>
  <div class="hline dash" style="left:0;top:96px;width:79px"></div>
  <div class="hline" style="left:287px;top:96px;width:79px"></div>
  <div class="frame-o" style="left:79px;top:53px;width:208px;height:88px"></div>
  <div class="abs" style="left:103px;top:46px;padding:0 4px;background:#fff;font-size:9px;font-weight:700;color:var(--purple)">Pelminor</div>
  <div class="abs" style="left:180px;top:43px;width:18px;height:18px;border-radius:50%;background:#3d9b4f;border:2px solid #fff"></div>
  <div class="abs" style="left:239px;top:46px;width:22px;height:13px;border-radius:6px;background:var(--orange);border:2px solid #fff"></div>
  <div class="tile" style="left:89px;top:67px;width:32px;height:21px;font-size:4px">Switch &amp;<br>CMS</div>
  <div class="tile" style="left:126px;top:67px;width:30px;height:21px;font-size:4px">POS<br>Pre-Host</div>
  <div class="tile" style="left:161px;top:67px;width:30px;height:21px;font-size:3.7px">Pelminor<br>APIs</div>
  <div class="tile" style="left:196px;top:67px;width:39px;height:21px;font-size:3.4px">API Stack<br>&amp;<br>Resource Portal</div>
  <div class="tile" style="left:240px;top:67px;width:42px;height:21px;font-size:3.5px">Merchant Poertal<br>Server</div>
  <div class="tile" style="left:89px;top:102px;width:32px;height:22px;font-size:4px">E-KYC<br>Host</div>
  <div class="tile" style="left:126px;top:102px;width:30px;height:22px;font-size:4px">Vexpay<br>Appliance</div>
  <div class="tile" style="left:161px;top:102px;width:30px;height:22px;font-size:4px">HSM</div>
  <div class="tile" style="left:196px;top:102px;width:30px;height:22px;font-size:3.6px">POS<br>Simulator</div>
  <div class="tile" style="left:231px;top:102px;width:46px;height:22px;font-size:3.5px">ATM Sim &amp; Scenario<br>Builder</div>
  <div class="legend" style="left:79px;top:146px;width:56px;height:37px"><div class="h">Payment network</div><div class="hline" style="left:7px;top:21px;width:22px;border-color:#333"></div><div class="abs" style="left:33px;top:18px">Online</div><div class="hline dash" style="left:7px;top:29px;width:22px;border-color:#333"></div><div class="abs" style="left:33px;top:26px">Offline</div></div>
  <div class="vline" style="left:183px;top:141px;height:24px"></div>
  <div class="hline" style="left:183px;top:165px;width:47px"></div>
  <svg class="ic" style="left:196px;top:158px" width="14" height="10"><use href="#i-cloud"/></svg>
  <div class="abs" style="left:193px;top:174px;font-size:5px;color:#555">Internet</div>
  <div class="frame-b" style="left:230px;top:146px;width:56px;height:39px"></div>
  <svg class="ic" style="left:239px;top:152px" width="17" height="17"><use href="#i-laptop"/></svg>
  <div class="abs" style="left:261px;top:151px;width:17px;height:17px;border-radius:50%;background:#8bc34a" role="img" aria-label="Illustrated customer avatar"></div>
  <div class="cap" style="left:230px;top:173px;width:56px">Institution Merchant</div>
  <div class="foot">© Pelminor Pte. Ltd.</div><div class="page">page <em>7</em></div>
</section>

<!-- Client institutions -->
<section class="slide small" style="left:796px;top:567px">
  <div class="dash p" style="left:17px;top:13px;width:14px"></div><div class="dash o" style="left:35px;top:13px;width:6px"></div>
  <div class="slide-title">Pelminor Payment Ecosystem</div>
  <div class="slide-sub">#3. Pelminor Client Institutions</div>
  <div class="brand"><b>Pelminor</b><span>Online Payment Security</span></div>
  <div class="hline" style="left:0;top:96px;width:118px"></div>
  <svg class="ic" style="left:68px;top:87px" width="18" height="18"><use href="#i-lock"/></svg>
  <div class="abs" style="left:70px;top:109px;font-size:5px;font-weight:600">VPN</div>
  <div class="vline" style="left:118px;top:76px;height:77px"></div>
  <div class="hline" style="left:118px;top:76px;width:33px"></div>
  <div class="hline" style="left:118px;top:153px;width:73px"></div>
  <div class="frame-o" style="left:151px;top:55px;width:155px;height:41px"></div>
  <div class="badge" style="left:143px;top:45px;width:20px;height:20px"></div>
  <div class="abs" style="left:165px;top:44px;font-size:6px;font-weight:600">Institution 1</div>
  <svg class="ic" style="left:163px;top:62px" width="140" height="14"><use href="#i-pos" x="0" width="14"/><use href="#i-atm" x="27" width="14"/><use href="#i-bank" x="54" width="14"/><use href="#i-shop" x="81" width="14"/><use href="#i-server" x="112" width="14"/></svg>
  <div class="cap" style="left:158px;top:81px;width:24px;font-size:4.6px">POS</div><div class="cap" style="left:185px;top:81px;width:24px;font-size:4.6px">ATM</div><div class="cap" style="left:212px;top:81px;width:24px;font-size:4.6px">CBS</div><div class="cap" style="left:236px;top:80px;width:32px;font-size:4.6px">Merchant</div><div class="cap" style="left:266px;top:80px;width:36px;font-size:4.6px">Other host</div>
  <div class="frame-o" style="left:191px;top:133px;width:155px;height:41px"></div>
  <div class="badge" style="left:183px;top:123px;width:20px;height:20px"></div>
  <div class="abs" style="left:205px;top:122px;font-size:6px;font-weight:600">Institution 2</div>
  <svg class="ic" style="left:203px;top:140px" width="140" height="14"><use href="#i-pos" x="0" width="14"/><use href="#i-atm" x="27" width="14"/><use href="#i-bank" x="54" width="14"/><use href="#i-shop" x="81" width="14"/><use href="#i-server" x="112" width="14"/></svg>
  <div class="cap" style="left:198px;top:159px;width:24px;font-size:4.6px">POS</div><div class="cap" style="left:225px;top:159px;width:24px;font-size:4.6px">ATM</div><div class="cap" style="left:252px;top:159px;width:24px;font-size:4.6px">CBS</div><div class="cap" style="left:276px;top:158px;width:32px;font-size:4.6px">Merchant</div><div class="cap" style="left:306px;top:158px;width:36px;font-size:4.6px">Other host</div>
  <div class="legend" style="left:27px;top:140px;width:56px;height:37px"><div class="h" style="top:5px">Payment network</div><div class="hline" style="left:7px;top:21px;width:22px;border-color:#333"></div><div class="abs" style="left:33px;top:18px">Online</div><div class="hline dash" style="left:7px;top:29px;width:22px;border-color:#333"></div><div class="abs" style="left:33px;top:26px">Offline</div></div>
  <div class="foot">© Pelminor Pte. Ltd.</div><div class="page">page <em>8</em></div>
</section>
</body>
</html>
```